Online video and marketing company business cards

Need to get some new business cards designed to fit with our new logo. The cards should be professional, clean and simple.

Cards should have:

Name
Position
2 line address
telephone
mobile
email address
web address

We need to have our logo and if possible say what we do...
ONLINE FILM PRODUCTION & STRATEGY

Marketing

```html
<!DOCTYPE html>
<html lang="en">
<head>
<meta charset="utf-8">
<title>Business cards</title>
<link rel="stylesheet" href="https://fonts.googleapis.com/css2?family=Mulish:wght@400;500;700&display=swap">
<style>
  :root {
    --backdrop: #4b4b4b;
    --card-white: #f7f7f5;
    --card-navy: #1b4163;
    --card-navy-deep: #163553;
    --brand-teal: #3b8ea8;
    --ink-navy: #1d3a5c;
    --ink-grey: #5a6470;
    --tagline: #d9e1e9;
    --mark-white: #f2f4f6;
  }
  * { margin: 0; padding: 0; box-sizing: border-box; }
  html, body {
    width: 1200px; height: 1000px; overflow: hidden;
    background: var(--backdrop);
    font-family: "Mulish", sans-serif;
  }
  .canvas { position: relative; width: 1200px; height: 1000px; }
  .card {
    position: absolute;
    border-radius: 16px;
    box-shadow: 0 6px 14px rgba(0,0,0,0.35);
  }
  .card-front {
    left: 192px; top: 172px; width: 528px; height: 302px;
    background: var(--card-white);
  }
  .card-back {
    left: 487px; top: 558px; width: 530px; height: 302px;
    background: linear-gradient(160deg, var(--card-navy) 0%, var(--card-navy-deep) 100%);
  }
  .brand {
    position: absolute;
    display: flex; align-items: center; gap: 12px;
  }
  .brand-dot {
    width: 40px; height: 40px; border-radius: 50%;
  }
  .brand-name {
    font-weight: 700; font-size: 44px; letter-spacing: -0.5px;
    color: var(--brand-teal); line-height: 1;
  }
  .card-front .brand { left: 206px; top: 82px; }
  .card-front .brand-dot { background: var(--ink-navy); }
  .card-back .brand { left: 202px; top: 86px; }
  .card-back .brand-dot { background: var(--mark-white); }

  .person { position: absolute; left: 38px; top: 228px; }
  .person-name {
    font-weight: 700; font-size: 15px; letter-spacing: 0.5px; color: var(--ink-navy);
  }
  .person-role { font-size: 13px; color: var(--ink-grey); margin-top: 1px; }

  .contact {
    position: absolute; right: 39px; top: 229px;
    text-align: right; font-size: 12px; line-height: 15px; color: var(--ink-navy);
  }
  .contact b { font-weight: 700; }

  .tagline {
    position: absolute; right: 45px; top: 208px;
    text-align: right; font-size: 14px; line-height: 18px;
    letter-spacing: 0.4px; color: var(--tagline);
  }
</style>
</head>
<body>
<main class="canvas">
  <section class="card card-front">
    <div class="brand">
      <span class="brand-dot"></span>
      <span class="brand-name">brightreel</span>
    </div>
    <div class="person">
      <p class="person-name">MORGAN HALE</p>
      <p class="person-role">Manager</p>
    </div>
    <div class="contact">
      <p>14, Larkfield Row, London N4 2QT U.K.</p>
      <p><b>M:</b> +44(0)207 555 0182 · <b>T:</b> +44(0)203 555 0147</p>
      <p><b>E:</b> hello@brightreel.com <b>W:</b> www.brightreel.com</p>
    </div>
  </section>

  <section class="card card-back">
    <div class="brand">
      <span class="brand-dot"></span>
      <span class="brand-name">brightreel</span>
    </div>
    <p class="tagline">ONLINE FILM PRODUCTION<br>&amp; STRATEGY</p>
  </section>
</main>
</body>
</html>
```